San Francisco Leading Consulting firm - 47Nova Web Design Project

•Create a Web Design
•Uncoded webpage layout design
•2 Pages Design - Homepage + Interior Page

Task Description
Hello, we're looking for a re-design our current website www.47nova-example.com

we have a sample mockup design @

http://47nova.civicpane-example.org/

This shows the layout that we like and also a sample of 6 pictures that would change based on where you mouse over..

6 pictures HOME design needs to be included.

SMART
THOUGHTFUL
FLEXIBLE
CREATIVE SERVICES
TECHNICAL SERVICES
PARTNERS

sites we like:

http://www.brelmoradvisory-example.com/Home.cfm?id=Home
http://www.pixelquarry-example.com/index.html

Our company can be best described as: 100+ employees, cutting-edge, depandable, innovative, strong, smart.

Our Primary focus is: IT Consulting Services and Creative Design services

47Nova LLC is a consulting firm providing creative design, business and technology solutions to both private and public interests.

Established in 1996, 47Nova is a San Francisco based company providing specialists for a range of business needs including:

Creative Design Services
•Print
•Logo Design
•Website Design
•Illustration

and

Business and Technology solutions

•Application Software and Web Development
•Business Process Re-Design (BPR)
•Business/Systems Analysis and Requirement Documentation
•Mentoring and Training
•Network/Hardware Installation Services
•System Design and Architecture
•Vendor Management
•Teamvault Architecture and Implementation

our sample mockup site:

Reason: Due to holiday season, we're not available to work with designers and finilize our design.  

Thank you very much for submitting your design.

We appreciate your time and creativity.   Since, our office is currently closed for holidays, we will be reviewing it in details next week and will make our decision as soon as possible.

It would be great if you could submit any of your changes by Wed next week, so it would be part of our reviews. 

Please see updated wireframe under attachments:  we have some minor updates to our wireframe that we would like you to update your designs, if possible.  

We also encorouge you not to use our standard wireframe and come up with more unique designs.   Everything would be considered when we review your design.

 

Target Market(s)

Creative services and professional services clients, including government agencies

Industry/Entity Type

Business

Requirements
Must have
• Clean, professional look, easy navigation

```html
<!DOCTYPE html>
<html lang="en">
<head>
<meta charset="utf-8">
<title>47Nova – Home</title>
<link rel="stylesheet" href="https://fonts.googleapis.com/css2?family=Open+Sans:ital,wght@0,300;0,400;0,600;0,700;1,600;1,700&family=PT+Sans:wght@400;700&display=swap">
<style>
:root{
  --ink:#1b1b1b;
  --muted:#a9a9a9;
  --blue:#0e7dbd;
  --blue-dark:#0a67a0;
  --blue-bright:#19a8ea;
  --blue-active:#1b8fcf;
  --link:#1b77b8;
  --card-line:#d6d6d6;
  --footer-top:#3a3a3a;
  --footer-bottom:#0d0d0d;
  --footer-text:#e6e6e6;
}
*{box-sizing:border-box;margin:0;padding:0}
html,body{width:1200px;height:1108px;overflow:hidden;background:#fff}
body{position:relative;font-family:"Open Sans",sans-serif;color:var(--ink)}
.abs{position:absolute}

.topbar{left:0;top:0;width:1200px;height:25px;background:linear-gradient(#2b2b2b,#000)}
.login-label{left:690px;top:5px;font:700 11px "Open Sans",sans-serif;color:#fff}
.login-field{top:4px;width:115px;height:17px;background:#fff;border:1px solid #888;font:10px "Open Sans",sans-serif;color:#333;padding:1px 4px;line-height:14px}
.login-go{left:1006px;top:5px;font:700 11px "Open Sans",sans-serif;color:#fff}

.brand{left:160px;top:78px;display:flex;align-items:center;gap:16px}
.brand-dot{width:50px;height:50px;border-radius:50%;background:var(--blue)}
.brand-name{font:300 46px "Open Sans",sans-serif;letter-spacing:3px;color:#444}

.address{right:175px;top:58px;text-align:right;font:400 12.5px/14px "Open Sans",sans-serif;color:var(--muted)}

.mainnav{left:156px;top:178px;width:886px;height:44px;display:flex;background:var(--blue)}
.mainnav a{flex:1;display:flex;align-items:center;justify-content:center;font:400 17px "PT Sans",sans-serif;color:#fff;text-decoration:none;border-right:1px solid #2a90c9}
.mainnav a:last-child{border-right:0}
.mainnav a.active{background:var(--blue-active);color:#111}
.dropdown{left:689px;top:222px;width:177px;height:85px;background:var(--blue-active);padding:9px 12px;list-style:none}
.dropdown li{font:400 13.5px/25px "PT Sans",sans-serif;color:#fff;border-left:2px solid #fff;padding-left:8px;height:25px;line-height:16px;margin-bottom:0;display:flex;align-items:center}
.dropdown li{border-left:none}
.dropdown li::before{content:"";width:1px;height:13px;background:#fff;margin-right:9px}

.hero{left:156px;top:223px;width:886px;height:295px;background:radial-gradient(ellipse at 30% 40%,#3b3b3b 0%,#151515 55%,#050505 100%)}
.hero-quote{left:673px;top:346px;width:369px;height:117px;background:rgba(12,80,125,.78)}
.hero-quote p{position:absolute;left:47px;top:26px;font:300 26px/33px "Open Sans",sans-serif;color:#fff}
.hero-quote p span{display:block;padding-left:40px}
.qmark{font:700 30px "Open Sans",sans-serif;color:#fff;position:absolute}

.tabs{left:156px;top:521px;width:886px;height:65px;display:flex}
.tab{flex:1;display:flex;align-items:center;justify-content:center;font:400 21px "PT Sans",sans-serif;color:#fff;border-right:1px solid rgba(255,255,255,.25)}
.tab:last-child{border-right:0}
.tab-peak{left:600px;top:492px}

.card{top:622px;width:296px;height:255px;border:1px solid var(--card-line);background:#fff}
.card-head{position:absolute;left:3px;top:1px;right:3px;height:28px;background:var(--blue);font:300 19px/28px "Open Sans",sans-serif;color:#fff;padding-left:15px}
.card-photo{position:absolute;left:3px;top:30px;right:3px;height:116px}
.card-caption{position:absolute;left:3px;top:96px;right:3px;height:50px;background:rgba(40,40,40,.72);font:italic 700 20px/50px "Open Sans",sans-serif;color:#fff;padding-left:13px;letter-spacing:-.3px}
.card-text{position:absolute;left:13px;right:13px;top:153px;font:400 11.5px/13.5px "Open Sans",sans-serif;color:#333;text-align:justify}
.card-more{position:absolute;right:14px;bottom:6px;font:italic 700 12.5px "Open Sans",sans-serif;color:var(--link)}

.footer{left:0;top:912px;width:1200px;height:196px;background:linear-gradient(var(--footer-top),var(--footer-bottom) 70%);border-top:2px solid #999}
.fcol{top:918px;width:234px}
.fcol h3{font:italic 400 16px/26px "PT Sans",sans-serif;color:#fff;text-align:center;border-bottom:1px solid #555;padding-bottom:2px}
.fcol ul{list-style:none;margin-top:8px}
.fcol li{font:400 12px/22px "Open Sans",sans-serif;color:var(--footer-text)}
.social{display:grid;grid-template-columns:repeat(3,27px);gap:9px 9px;margin:10px 0 0 10px}
.social span{width:27px;height:27px;border-radius:3px;background:#f3f3f3}
.copyright{left:0;top:1074px;width:1200px;text-align:center;font:400 12px "Open Sans",sans-serif;color:#fff}
</style>
</head>
<body>

<div class="abs topbar"></div>
<div class="abs login-label">Client Login</div>
<div class="abs login-field" style="left:758px">username</div>
<div class="abs login-field" style="left:877px">password</div>
<div class="abs login-go">GO</div>

<div class="abs brand"><span class="brand-dot"></span><span class="brand-name">47NOVA</span></div>

<address class="abs address" style="font-style:normal">
47Nova, LLC<br>2250 Harbor Lane, Suite 400<br>San Francisco, CA 94111<br><br>Phone: 1-415-555-0142<br>Fax: 1-415-555-0143
</address>

<nav class="abs mainnav">
  <a href="#">Our Company</a>
  <a href="#">Technical Services</a>
  <a href="#">Creative Services</a>
  <a href="#" class="active">Our Partners</a>
  <a href="#">Contact Us</a>
</nav>

<div class="abs hero" role="img" aria-label="Row of light bulbs on a dark background, one bulb glowing"></div>
<ul class="abs dropdown">
  <li>Vendor Relationships</li>
  <li>Strategic Partners</li>
  <li>Become our Partner</li>
</ul>
<div class="abs hero-quote">
  <span class="qmark" style="left:26px;top:8px">“</span>
  <p>Some Words<span>Of Inspiration Here</span></p>
  <span class="qmark" style="right:42px;top:42px">”</span>
</div>

<svg class="abs tab-peak" width="148" height="32" viewBox="0 0 148 32">
  <polygon points="0,32 74,2 148,32" fill="#1592d6"/>
  <polyline points="0,31 74,2 148,31" fill="none" stroke="#fff" stroke-width="3"/>
</svg>
<div class="abs tabs">
  <div class="tab" style="background:#0a6aa5">SMART</div>
  <div class="tab" style="background:#0c77b6">THOUGHTFUL</div>
  <div class="tab" style="background:#0f84c5">FLEXIBLE</div>
  <div class="tab" style="background:#1592d6">CREATIVE</div>
  <div class="tab" style="background:#179ee2">TECHNICAL</div>
  <div class="tab" style="background:#1aa9ed">PARTNERS</div>
</div>

<section class="abs card" style="left:156px">
  <div class="card-head">For Graphic Designers</div>
  <div class="card-photo" role="img" aria-label="Hand drawing with a stylus on a graphics tablet" style="background:linear-gradient(120deg,#f2f2f2,#8a8a8a 60%,#3a3a3a)"></div>
  <div class="card-caption">Get Creative!</div>
  <p class="card-text">47Nova is looking for top creative talent to deliver graphic design solutions for some leading global brands Do you have what it takes?</p>
  <span class="card-more">Learn More...</span>
</section>

<section class="abs card" style="left:453px">
  <div class="card-head">For Clients</div>
  <div class="card-photo" role="img" aria-label="Hands holding a blue globe" style="background:radial-gradient(circle at 50% 35%,#33aee8,#6fb6d6 40%,#e8e8e8 75%)"></div>
  <div class="card-caption">The 47Nova Diference</div>
  <p class="card-text">Smart, Flexible, Thoughtful: find out why leading corporations and government agencies are turning to 47nova to help manage their most demanding IT services challenges.</p>
  <span class="card-more">Learn More...</span>
</section>

<section class="abs card" style="left:748px">
  <div class="card-head">For Partners</div>
  <div class="card-photo" role="img" aria-label="Two business people shaking hands" style="background:linear-gradient(90deg,#2a2a2a,#9a8070 50%,#3a3a3a)"></div>
  <div class="card-caption">Team Up With The Best</div>
  <p class="card-text">When it comes to technology partnerships, our mission it so make you a success.</p>
  <span class="card-more">Learn More...</span>
</section>

<footer class="abs footer"></footer>
<div class="abs fcol" style="left:188px">
  <h3>Follow Us</h3>
  <div class="social"><span></span><span></span><span></span><span></span><span></span><span></span></div>
</div>
<div class="abs fcol" style="left:491px">
  <h3>Company</h3>
  <ul style="padding-left:22px"><li>Sitemap</li><li>Support</li><li>Contact Us</li><li>Privacy Policy</li></ul>
</div>
<div class="abs fcol" style="left:778px">
  <h3>Related Links</h3>
  <ul style="padding-left:21px"><li>Related Link 1</li><li>Related Link 2</li><li>Related Link 3</li><li>Related Link 4</li></ul>
</div>
<div class="abs copyright">Copyright 2010, 47Nova, LLC All rights reserved</div>

</body>
</html>
```